Disability Service Provider Website

We are working with VEP, which provides services and job training designed to educate, facilitate, train, and assist individuals with disabilities. They describe their clients using words like Unity and Unique.
Some sites to use for content/competitors and inspiration:
https://www.skillmora.com
https://www.pwkd.org
https://www.bellowhaven.org
https://www.openmeadow.org
https://corvelan.org
Thank you for taking the time to consider designing a website for us. We are web developers based in Stockton, CA, USA. Most of our projects go through the same process. Understanding this process may help you win a project with us. We custom-code all of our websites in-house. We don’t have any requirements as to what tools you use for your design, but we prefer Figma files. For any design that we label as four-stars, we send it to the client for review. The client picks the final design they want us to use. Once we complete this process, we will continue to show additional clients all the four-star sites and purchase them later. Your designs will have multiple chances to sell. For better chances of success, we ask that you follow these guidelines.
IMAGES:
If you use any images or icons in the design, we ask that you have a link to the asset so we can purchase the image/icon. Most of the designs we submit do not have the customer’s images on them unless they have some great images. Be creative; show us the feeling you are trying to portray with your image choices. Use any royalty-free site you choose. We subscribe to Stellic and mainly use their images, but we can purchase images outside of Stellic.
PLEASE NOTE: we will not submit designs to clients with watermarks on the images.
FONTS:
We ask that you identify the fonts used in the design. This can be done in a message if you want. We typically use Bramble Fonts and Stellic Fonts.
CONTENT:
We're always open to different content and ideas. We often submit designs with stock images so the client can see our vision. We typically take pictures after the website launch to use their images with our vision. Lorem Ipsum is fine for paragraphs, but we ask that you write the headers in correct English. We want to be able to show the vision and identify the sections of the website.
INSPIRATION:
We typically add a couple of links in the brief of websites we like to help you get started in your design.
REVISIONS:
We do not often ask for revisions of the designs unless we see something in the design that may not appeal to the client. If there are slight changes that we want to make, we do that in the development process.
FEEDBACK:
We rarely give feedback on designs during the design process. We are working on many website projects and do not have the time to provide feedback. We usually respond if your request is well thought out and asks specific questions, but a note asking “feedback, please” usually goes unanswered.
Number of Pages Required
1 page
Look and feel
Each slider illustrates characteristics of the customer's brand and the style your logo design should communicate.

```html
<!DOCTYPE html>
<html lang="en">
<head>
<meta charset="utf-8">
<title>VEP — Services and Job Training</title>
<link href="https://fonts.googleapis.com/css2?family=Poppins:wght@400;500;600;700&display=swap" rel="stylesheet">
<style>
:root{
  --red:#a31616;
  --red-dark:#8f0f0f;
  --red-bright:#c41a1a;
  --ink:#2b2b2b;
  --muted:#555;
  --light:#f6f4f4;
  --white:#fff;
}
*{box-sizing:border-box;margin:0;padding:0}
html,body{width:1200px;height:5199px;overflow:hidden}
body{font-family:'Poppins',sans-serif;color:var(--ink);background:var(--white);position:relative}
.abs{position:absolute}
a{color:inherit;text-decoration:none}
.btn{position:absolute;display:flex;align-items:center;justify-content:center;gap:12px;border-radius:30px;background:var(--red);color:var(--white);font-weight:600;font-size:16px;letter-spacing:.3px}
.arrow{width:34px;height:10px}
.rule{position:absolute;height:10px;width:60px}
.rule::before{content:"";position:absolute;left:0;right:0;top:4px;height:2px;background:var(--red)}
.rule::after{content:"";position:absolute;left:50%;top:0;width:10px;height:10px;margin-left:-5px;border-radius:50%;background:var(--red)}
.rule.left::after{left:5px}
.rule.white::before,.rule.white::after{background:var(--white)}
.section-title{position:absolute;left:0;width:1200px;text-align:center;font-size:52px;font-weight:500;color:var(--ink)}
.lorem{font-size:13px;line-height:22px;color:var(--muted)}

/* top bar */
.topbar{left:0;top:0;width:1200px;height:40px;background:var(--red);color:var(--white);font-size:12px}
.search{left:528px;top:6px;width:192px;height:28px;border:1.5px solid var(--white);border-radius:16px;padding-left:18px;line-height:25px}
.search svg{position:absolute;right:10px;top:5px}
.top-item{top:0;height:40px;display:flex;align-items:center;gap:10px}

/* nav */
.logo{font-weight:700;color:var(--red);letter-spacing:1px}
.nav a{position:absolute;top:76px;font-size:13px;color:var(--ink)}
.nav a.active::after{content:"";position:absolute;left:0;right:0;bottom:-6px;height:1.5px;background:var(--ink)}

/* hero */
.hero-photo{left:0;top:135px;width:1185px;height:722px;background:linear-gradient(90deg,#c9c2bd 0%,#e6e2e0 35%,#f3f2f2 60%,#e8e8ea 100%)}
.hero-glow{left:460px;top:135px;width:620px;height:722px;background:radial-gradient(ellipse at 55% 45%,rgba(255,255,255,.95) 0%,rgba(255,255,255,.75) 45%,rgba(255,255,255,0) 72%)}
.hero-text{left:520px;top:310px;width:600px;text-align:center}
.hero-text h1{color:var(--red);font-size:50px;line-height:64px;font-weight:700}
.hero-text p{font-size:29px;line-height:44px;color:var(--ink);margin-top:2px}
.hero-text strong{display:block;font-size:38px;font-weight:700;line-height:46px}

/* stats */
.stat{position:absolute;top:1140px;display:flex;gap:14px}
.stat-icon{width:76px;height:76px;border-radius:50%;border:2px solid var(--red);display:flex;align-items:center;justify-content:center;flex:none}
.stat-icon span{width:60px;height:60px;border-radius:50%;background:var(--red);display:flex;align-items:center;justify-content:center}
.stat-num{font-size:48px;font-weight:600;color:var(--red);line-height:1}
.stat-txt{font-size:12px;line-height:15px;color:var(--ink);width:175px;margin-top:6px}

/* who */
.who-photo{left:597px;top:1412px;width:528px;height:389px;border-radius:0 0 40px 0;background:linear-gradient(135deg,#d8d2cc,#8a7a72 55%,#c4bdb6)}
.play{left:577px;top:1705px;width:100px;height:100px;border-radius:50%;background:#eee;display:flex;align-items:center;justify-content:center}

/* services */
.service{position:absolute;top:2259px;width:245px}
.service h3{font-size:34px;font-weight:500;margin-top:28px;color:var(--ink)}
.service p{font-size:13px;line-height:22px;color:var(--muted);margin-top:16px}
.service .more{display:flex;align-items:center;gap:8px;margin-top:18px;font-size:12px;font-weight:600;color:var(--red)}

/* events */
.events-photo{left:0;top:2697px;width:1200px;height:645px;background:linear-gradient(90deg,#6a4a3c 0%,#a97c62 35%,#c9a68a 60%,#7a4a5a 100%)}
.events-figure{left:766px;top:2562px;width:434px;height:780px;border-radius:200px 0 0 0;background:linear-gradient(180deg,#b9876a 0%,#6d3f55 60%,#5a2f45 100%)}
.events-card{left:73px;top:2818px;width:597px;height:466px;border-radius:20px;background:rgba(160,20,20,.72);color:var(--white)}
.events-card h2{position:absolute;left:50px;top:44px;font-size:56px;line-height:65px;font-weight:500}
.events-card p{position:absolute;left:60px;top:232px;width:400px;font-size:13px;line-height:22px}
.btn-outline{background:transparent;border:2px solid var(--white)}

/* reviews */
.review-card{left:135px;top:3588px;width:934px;height:309px;border:2px solid var(--red);border-radius:30px}
.quote-mark{left:228px;top:3598px;font-size:150px;line-height:1;color:#ddd;font-family:'Poppins',sans-serif}
.review-text{left:220px;top:3666px;width:760px;text-align:center;font-size:15px;line-height:27px;color:var(--ink)}
.avatar{left:490px;top:3788px;width:68px;height:68px;border-radius:50%;background:radial-gradient(circle,#b78d6e,#5b3b2b)}
.nav-circle{width:30px;height:30px;border-radius:50%;border:1px solid #ccc;display:flex;align-items:center;justify-content:center;background:var(--white)}
.dot{width:11px;height:11px;border-radius:50%;border:1.5px solid var(--ink)}
.dot.on{background:var(--ink)}

/* contact */
.contact-bg{left:0;top:4028px;width:1200px;height:722px;background:var(--light)}
.contact-red{left:916px;top:4028px;width:284px;height:722px;background:var(--red)}
.contact-ring{left:636px;top:4113px;width:556px;height:556px;border-radius:50%;border:3px solid var(--red);background:var(--white)}
.contact-photo{left:650px;top:4127px;width:528px;height:528px;border-radius:50%;background:linear-gradient(135deg,#e9e7e6,#b9aaa0 50%,#d9d4d2)}
.field{position:absolute;background:var(--white);border:1px solid #e2e0e0;font-size:12px;color:#999;padding:14px 20px}

/* footer */
.footer{left:0;top:4750px;width:1200px;height:383px;background:var(--red-dark);color:var(--white)}
.footer h4{position:absolute;top:123px;font-size:15px;font-weight:500;letter-spacing:.3px}
.footer .rule{top:150px;width:36px}
.footer .rule::after{left:4px}
.qlinks a{position:absolute;left:341px;font-size:13px;display:flex;align-items:center;gap:8px}
.c-item{position:absolute;left:571px;display:flex;gap:16px;font-size:12px;line-height:15px}
.c-icon{width:28px;height:28px;border:1px solid var(--white);border-radius:4px;display:flex;align-items:center;justify-content:center;flex:none}
.social{position:absolute;top:282px;width:28px;height:28px;border:1px solid var(--white);border-radius:3px}
.social span{position:absolute;left:8px;top:8px;width:10px;height:10px;background:var(--white);border-radius:2px}
.copyright{left:0;top:5133px;width:1200px;height:66px;background:var(--red-bright);color:var(--white);font-size:12px;display:flex;align-items:center;justify-content:center}
</style>
</head>
<body>

<!-- top bar -->
<div class="abs topbar">
  <div class="abs search">SEARCH
    <svg width="18" height="18" viewBox="0 0 18 18" fill="none" stroke="#fff" stroke-width="2"><circle cx="7.5" cy="7.5" r="5.5"/><path d="M12 12l5 5"/></svg>
  </div>
  <div class="abs top-item" style="left:785px">
    <svg width="18" height="18" viewBox="0 0 24 24" fill="#fff"><path d="M6.6 10.8a15 15 0 006.6 6.6l2.2-2.2a1 1 0 011-.25 11.4 11.4 0 003.6.57 1 1 0 011 1V20a1 1 0 01-1 1A17 17 0 013 4a1 1 0 011-1h3.5a1 1 0 011 1c0 1.25.2 2.45.57 3.6a1 1 0 01-.25 1z"/></svg>
    XXXX XXX XXX</div>
  <div class="abs top-item" style="left:950px">
    <svg width="20" height="14" viewBox="0 0 20 14" fill="#fff"><rect width="20" height="14" rx="1"/><path d="M1 1l9 7 9-7" stroke="#a31616" stroke-width="1.6" fill="none"/></svg>
    info@vepcenter.org</div>
</div>

<!-- nav -->
<div class="abs logo" style="left:74px;top:44px;font-size:62px;line-height:80px">VEP</div>
<nav class="nav">
  <a class="active" style="left:375px">HOME</a>
  <a style="left:454px">WHO WE ARE</a>
  <a style="left:577px">WHAT WE DO</a>
  <a style="left:702px">JOIN US</a>
  <a style="left:793px">BLOG</a>
  <a style="left:865px">CONTACT US</a>
</nav>
<a class="btn" style="left:986px;top:58px;width:138px;height:47px;font-size:13px;font-weight:500">DONATE</a>

<!-- hero -->
<div class="abs hero-photo" role="img" aria-label="Smiling woman in a wheelchair holding a pink folder, colleagues presenting at a whiteboard behind"></div>
<div class="abs hero-glow"></div>
<div class="abs hero-text">
  <h1>PROVIDES SERVICES<br>AND JOB TRAINING</h1>
  <p>DESIGNED TO EDUCATE, FACILITATE,<br>TRAIN, AND ASSIST INDIVIDUALS WITH</p>
  <strong>DISABILITIES</strong>
</div>
<a class="btn" style="left:710px;top:621px;width:206px;height:51px">CONTACT US
  <svg class="arrow" viewBox="0 0 34 10" fill="none" stroke="#fff" stroke-width="2"><path d="M0 5h32M27 1l5 4-5 4"/></svg></a>

<!-- numbers -->
<h2 class="section-title" style="top:948px">Our Strength in Numbers in 2023</h2>
<div class="rule" style="left:570px;top:1043px"></div>

<div class="stat" style="left:104px">
  <div class="stat-icon"><span><svg width="20" height="34" viewBox="0 0 20 34" fill="#fff"><circle cx="10" cy="4" r="4"/><path d="M4 10h12v12h-3v12H7V22H4z"/></svg></span></div>
  <div><div class="stat-num">769</div><div class="stat-txt">people received 17,121 sessions of mental health support so far this year</div></div>
</div>
<div class="stat" style="left:446px">
  <div class="stat-icon"><span><svg width="32" height="32" viewBox="0 0 32 32" fill="none" stroke="#fff" stroke-width="2.4"><circle cx="13" cy="4" r="3" fill="#fff" stroke="none"/><path d="M13 8v10h9l4 8"/><path d="M9 14a8 8 0 1010 10"/></svg></span></div>
  <div><div class="stat-num">431</div><div class="stat-txt">people with disabilities received help with their job search</div></div>
</div>
<div class="stat" style="left:797px">
  <div class="stat-icon"><span><svg width="20" height="34" viewBox="0 0 20 34" fill="#fff"><circle cx="10" cy="4" r="4"/><path d="M4 10h12v12h-3v12H7V22H4z"/></svg></span></div>
  <div><div class="stat-num">719</div><div class="stat-txt">teachers and parents were reached through a partnership between KRN and MWA</div></div>
</div>

<!-- who we are -->
<h2 class="abs" style="left:76px;top:1440px;font-size:52px;font-weight:500">Who We Are</h2>
<div class="rule left" style="left:80px;top:1522px"></div>
<p class="abs lorem" style="left:83px;top:1580px;width:445px">Lorem ipsum dolor sit amet, consectetur adipiscing elit, sed do eiusmod tempor incididunt ut labore et dolore magna aliqua. Ut enim ad minim veniam, quis nostrud exercitation ullamco laboris nisi ut aliquip ex ea commodo consequat. Duis aute irure dolor in reprehenderit in voluptate velit ess</p>
<a class="btn" style="left:81px;top:1751px;width:215px;height:52px">LEARN MORE
  <svg class="arrow" viewBox="0 0 34 10" fill="none" stroke="#fff" stroke-width="2"><path d="M0 5h32M27 1l5 4-5 4"/></svg></a>
<div class="abs who-photo" role="img" aria-label="Two men shaking hands in an office, one seated in a wheelchair"></div>
<div class="abs play"><svg width="30" height="32" viewBox="0 0 30 32"><path d="M4 2l24 14L4 30z" fill="#a31616"/></svg></div>

<!-- what we do -->
<h2 class="section-title" style="top:1980px">What We do</h2>
<div class="rule" style="left:570px;top:2074px"></div>
<p class="abs" style="left:0;top:2130px;width:1200px;text-align:center;font-size:22px;line-height:27px;color:var(--ink)">We are working with VEP, which provides services and job training designed to educate,<br>facilitate, train, and assist individuals with disabilities</p>

<div class="service" style="left:75px">
  <svg width="90" height="60" viewBox="0 0 90 60" fill="#a31616"><path d="M45 4L2 20l43 16 43-16z"/><path d="M20 30v16c8 8 42 8 50 0V30L45 40z"/><path d="M82 22v22" stroke="#a31616" stroke-width="3"/></svg>
  <h3>Educate</h3>
  <p>Lorem ipsum dolor sit amet, cons ectetur adipiscing elit, sed do eius mod tempor incididunt</p>
  <div class="more">LEARN MORE <svg width="22" height="10" viewBox="0 0 22 10" fill="none" stroke="#a31616" stroke-width="2"><path d="M0 5h20M16 1l4 4-4 4"/></svg></div>
</div>
<div class="service" style="left:343px">
  <svg width="80" height="62" viewBox="0 0 80 62" fill="#a31616"><circle cx="28" cy="26" r="18"/><circle cx="28" cy="26" r="7" fill="#fff"/><g stroke="#a31616" stroke-width="7"><path d="M28 2v8M28 42v8M4 26h8M44 26h8M11 9l6 6M39 37l6 6M11 43l6-6M39 15l6-6"/></g><circle cx="58" cy="46" r="14" fill="#fff" stroke="#a31616" stroke-width="3"/><circle cx="58" cy="42" r="4"/><path d="M50 54a8 6 0 0116 0z"/></svg>
  <h3>Facilitate</h3>
  <p>Lorem ipsum dolor sit amet, cons ectetur adipiscing elit, sed do eius mod tempor incididunt</p>
  <div class="more">LEARN MORE <svg width="22" height="10" viewBox="0 0 22 10" fill="none" stroke="#a31616" stroke-width="2"><path d="M0 5h20M16 1l4 4-4 4"/></svg></div>
</div>
<div class="service" style="left:629px">
  <svg width="70" height="60" viewBox="0 0 70 60" fill="#a31616"><circle cx="12" cy="8" r="7"/><path d="M2 18h20v22H2z"/><rect x="26" y="14" width="40" height="30" fill="none" stroke="#a31616" stroke-width="3"/><path d="M32 36l10-10 6 6 12-12" fill="none" stroke="#a31616" stroke-width="3"/><path d="M2 42h64v5H2z"/></svg>
  <h3>Training</h3>
  <p>Lorem ipsum dolor sit amet, cons ectetur adipiscing elit, sed do eius mod tempor incididunt</p>
  <div class="more">LEARN MORE <svg width="22" height="10" viewBox="0 0 22 10" fill="none" stroke="#a31616" stroke-width="2"><path d="M0 5h20M16 1l4 4-4 4"/></svg></div>
</div>
<div class="service" style="left:900px">
  <svg width="64" height="60" viewBox="0 0 64 60" fill="none" stroke="#a31616" stroke-width="5" stroke-linecap="round"><path d="M8 56l20-22M20 30l16-24M28 38l22-22M34 44l22-16M12 50c10-6 30-4 42-20"/></svg>
  <h3>Assist</h3>
  <p>Lorem ipsum dolor sit amet, cons ectetur adipiscing elit, sed do eius mod tempor incididunt</p>
  <div class="more">LEARN MORE <svg width="22" height="10" viewBox="0 0 22 10" fill="none" stroke="#a31616" stroke-width="2"><path d="M0 5h20M16 1l4 4-4 4"/></svg></div>
</div>

<!-- events -->
<div class="abs events-photo" role="img" aria-label="Group of young people drawing with colored pencils at a table"></div>
<div class="abs events-figure" role="img" aria-label="Smiling young woman with glasses in a purple sweater"></div>
<div class="abs events-card">
  <h2>Upcoming Events<br>and Trainings</h2>
  <div class="rule left white" style="left:60px;top:190px"></div>
  <p>Lorem ipsum dolor sit amet, cons ectetur adipiscing elit, sed do eiusmod tempor incididuntut labore et dolore magna aliqua. Ut enim ad minim veniam, quis nostru exercitation ullamco laboris nisi ut aliquip</p>
  <a class="btn btn-outline" style="left:60px;top:359px;width:262px;height:52px">VIEW FULL SCHEDULE
    <svg class="arrow" viewBox="0 0 34 10" fill="none" stroke="#fff" stroke-width="2"><path d="M0 5h32M27 1l5 4-5 4"/></svg></a>
</div>

<!-- reviews -->
<h2 class="section-title" style="top:3414px">Client Reviews</h2>
<div class="rule" style="left:570px;top:3512px"></div>
<div class="abs review-card"></div>
<div class="abs quote-mark">“</div>
<p class="abs review-text">Lorem ipsum dolor sit amet, consectetur adipiscing elit, sed do eiu smod tempor incididunt ut labore et dolore magna aliqua. Quis ipsum suspendisse ultrices gravida. Risus commodo viverra maecenas accumsan lacus vel facilisis.</p>
<div class="abs avatar" role="img" aria-label="Client portrait"></div>
<div class="abs" style="left:579px;top:3808px;font-size:15px;font-weight:500">Marcus Ellery</div>
<div class="abs" style="left:580px;top:3832px;font-size:12px;color:#f2b705;letter-spacing:1px">★★★★★</div>
<div class="abs nav-circle" style="left:60px;top:3727px"><svg width="8" height="10" viewBox="0 0 8 10" fill="none" stroke="#333" stroke-width="1.6"><path d="M6 1L2 5l4 4"/></svg></div>
<div class="abs nav-circle" style="left:1113px;top:3727px"><svg width="8" height="10" viewBox="0 0 8 10" fill="none" stroke="#333" stroke-width="1.6"><path d="M2 1l4 4-4 4"/></svg></div>
<div class="abs" style="left:572px;top:3942px;display:flex;gap:12px"><span class="dot"></span><span class="dot on"></span><span class="dot"></span></div>

<!-- contact -->
<div class="abs contact-bg"></div>
<div class="abs contact-red"></div>
<div class="abs contact-ring"></div>
<div class="abs contact-photo" role="img" aria-label="Team meeting at a whiteboard with a colleague in a wheelchair"></div>
<h2 class="abs" style="left:75px;top:4080px;font-size:52px;font-weight:500">Contact Us</h2>
<div class="rule left" style="left:80px;top:4160px"></div>
<p class="abs lorem" style="left:81px;top:4243px;width:500px">Lorem ipsum dolor sit amet, consectetur adipiscing elit, sed do eiusmod tempor incididunt ut labore et dolore magna aliqua.</p>
<div class="field" style="left:75px;top:4322px;width:222px;height:45px">First Name</div>
<div class="field" style="left:317px;top:4322px;width:224px;height:45px">Last Name</div>
<div class="field" style="left:75px;top:4387px;width:222px;height:45px">Phone</div>
<div class="field" style="left:317px;top:4387px;width:224px;height:45px">Email</div>
<div class="field" style="left:75px;top:4453px;width:466px;height:142px;padding-top:24px">Mesage:</div>
<a class="btn" style="left:75px;top:4635px;width:169px;height:49px">SUBMIT
  <svg class="arrow" viewBox="0 0 34 10" fill="none" stroke="#fff" stroke-width="2" style="width:28px"><path d="M0 5h32M27 1l5 4-5 4"/></svg></a>

<!-- footer -->
<footer class="abs footer">
  <div class="abs" style="left:99px;top:130px;font-size:72px;font-weight:700;line-height:84px;letter-spacing:1px">VEP</div>
  <div class="social" style="left:101px"><span></span></div>
  <div class="social" style="left:141px"><span></span></div>
  <div class="social" style="left:180px"><span></span></div>
  <div class="social" style="left:220px"><span></span></div>

  <h4 style="left:341px">QUICK LINKS</h4>
  <div class="rule left white" style="left:341px"></div>
  <div class="qlinks">
    <a style="top:186px">» Who We Are</a>
    <a style="top:213px">» What We Do</a>
    <a style="top:240px">» Join Us</a>
    <a style="top:267px">» Blog</a>
    <a style="top:294px">» Donate</a>
  </div>

  <h4 style="left:571px">CONTACT US</h4>
  <div class="rule left white" style="left:571px"></div>
  <div class="c-item" style="top:186px"><span class="c-icon"><svg width="14" height="14" viewBox="0 0 24 24" fill="#fff"><path d="M6.6 10.8a15 15 0 006.6 6.6l2.2-2.2a1 1 0 011-.25 11.4 11.4 0 003.6.57 1 1 0 011 1V20a1 1 0 01-1 1A17 17 0 013 4a1 1 0 011-1h3.5a1 1 0 011 1c0 1.25.2 2.45.57 3.6a1 1 0 01-.25 1z"/></svg></span><span>CALL US<br>8012 555 0147</span></div>
  <div class="c-item" style="top:240px"><span class="c-icon"><svg width="14" height="10" viewBox="0 0 20 14" fill="#fff"><rect width="20" height="14" rx="1"/></svg></span><span>EMAIL US<br>hello@vepcenter.org</span></div>
  <div class="c-item" style="top:291px"><span class="c-icon"><svg width="12" height="16" viewBox="0 0 12 16" fill="#fff"><path d="M6 0a6 6 0 00-6 6c0 4.5 6 10 6 10s6-5.5 6-10a6 6 0 00-6-6zm0 8.5A2.5 2.5 0 116 3.5a2.5 2.5 0 010 5z"/></svg></span><span>Address line Dummy Here<br>Address line Here</span></div>

  <h4 style="left:877px">OUR NEWSLETTER</h4>
  <div class="rule left white" style="left:877px"></div>
  <p class="abs" style="left:877px;top:186px;width:230px;font-size:12px;line-height:16px">Subscribe our newsletter to get the latest news.</p>
  <div class="abs" style="left:867px;top:242px;width:212px;height:35px;border:1px solid #fff;border-radius:18px;font-size:11px;padding:9px 18px">Enter Email Address
    <svg class="abs" style="right:8px;top:6px" width="22" height="22" viewBox="0 0 22 22" fill="none" stroke="#fff" stroke-width="1.4"><circle cx="11" cy="11" r="10"/><path d="M6 11h10M12 7l4 4-4 4"/></svg></div>
</footer>
<div class="abs copyright">Copyright © 2024 All Rights Reserved By Company name</div>

</body>
</html>
```